Detailing informational flyer

I want to design a new flyer for my automotive detailing business. The flyer should use the color scheme from the logo and be easy to read and understand the services we offer.

Industry/Entity Type

Automotive

Font styles to use
Serif
Sans Serif

Colors
3176b5
0255a3
fbed22
33a6d7
0692cd
ffffff

Requirements
Must have
• must include all information from the copy
Nice to have
• include a Glavenor logo such as the image attached

```html
<!DOCTYPE html>
<html lang="en">
<head>
<meta charset="utf-8">
<title>Ridgeview Carwash Detailing Center Flyer</title>
<link rel="stylesheet" href="https://fonts.googleapis.com/css2?family=Archivo:wght@700;800&family=Nunito:wght@400;600;800;900&display=swap">
<style>
  :root {
    --page-bg: #e8e7ee;
    --flyer-bg: #6dbbf2;
    --panel-top: #44b3ee;
    --panel-bottom: #2fa6e6;
    --panel-edge: #1f7fb8;
    --yellow: #fbed22;
    --navy: #0b2a55;
    --brand-blue: #0255a3;
    --white: #ffffff;
  }
  * { margin: 0; padding: 0; box-sizing: border-box; }
  html, body {
    width: 1200px; height: 1200px; overflow: hidden;
    background: var(--page-bg);
  }
  .flyer {
    position: absolute; left: 176px; top: 30px;
    width: 848px; height: 1140px;
    background: var(--flyer-bg);
    font-family: "Nunito", sans-serif;
    color: var(--white);
    box-shadow: 0 10px 30px rgba(20, 40, 80, 0.18);
  }
  .partner-name {
    position: absolute; left: 53px; top: 40px;
    font-family: "Nunito", sans-serif; font-weight: 900;
    font-size: 38px; line-height: 44px; letter-spacing: 0.5px;
    color: var(--brand-blue);
  }
  .title {
    position: absolute; left: 50px; top: 100px;
    font-family: "Nunito", sans-serif; font-weight: 800;
    font-size: 48px; line-height: 54px; color: var(--white);
  }
  .title span { display: block; }
  .title .second { padding-left: 4px; }
  .brand-name {
    position: absolute; left: 517px; top: 128px; width: 243px;
    text-align: center;
    font-family: "Nunito", sans-serif; font-weight: 900;
    font-size: 30px; line-height: 36px;
    color: var(--navy);
  }
  .headline {
    position: absolute; left: 0; right: 0; top: 255px;
    text-align: center;
    font-family: "Archivo", sans-serif; font-weight: 800;
    font-size: 25px; line-height: 32px; text-transform: uppercase;
    color: var(--white);
  }
  .service {
    position: absolute; left: 55px; width: 738px;
    background: linear-gradient(180deg, var(--panel-top), var(--panel-bottom));
    border-radius: 28px 34px 34px 28px;
    box-shadow: 0 3px 0 var(--panel-edge), 0 5px 8px rgba(10, 60, 110, 0.25);
  }
  .service-tag {
    position: absolute; left: -5px; top: 18px; height: 40px;
  }
  .service-tag svg { position: absolute; left: 0; top: 0; }
  .service-tag h2 {
    position: relative; height: 40px; line-height: 42px;
    font-family: "Archivo", sans-serif; font-weight: 800;
    font-size: 22px; color: var(--navy); text-transform: uppercase;
    white-space: nowrap;
  }
  .service p {
    position: absolute; left: 19px; right: 20px;
    font-size: 15.2px; line-height: 20.6px; font-weight: 600;
    color: var(--white);
  }
  .service p.justified { text-align: justify; letter-spacing: 0.55px; }
  .exterior { top: 324px; height: 149px; }
  .interior { top: 498px; height: 156px; }
  .mini { top: 686px; height: 214px; }
  .headlight { top: 924px; height: 150px; }
</style>
</head>
<body>
<main class="flyer">
  <div class="partner-name">Glavenor</div>

  <h1 class="title">
    <span>Ridgeview Carwash</span>
    <span class="second">Detailing Center.</span>
  </h1>

  <div class="brand-name">Ridgeview<br>Detail Center</div>

  <p class="headline">Ask to speak to a manager about scheduling<br>any of our detailing services.</p>

  <section class="service exterior">
    <div class="service-tag" style="width:458px">
      <svg width="458" height="40" viewBox="0 0 458 40"><polygon points="0,0 458,0 420,40 0,40" fill="#fbed22"/></svg>
      <h2 style="padding-left:40px">Exterior Detailing Includes:</h2>
    </div>
    <p style="top:68px">We wash, clay, compound, polish, and wax, as needed to restore the deep rich gloss and provide a durable shine for that “new car” look. This process removes light oxidation from the vehicle and protects the clear coat finish. Finishing touches include rim cleaning and tire shine.</p>
  </section>

  <section class="service interior">
    <div class="service-tag" style="width:568px">
      <svg width="568" height="40" viewBox="0 0 568 40"><polygon points="0,0 568,0 530,40 0,40" fill="#fbed22"/></svg>
      <h2 style="padding-left:21px">Interior Detailing Shampoo Includes:</h2>
    </div>
    <p class="justified" style="top:64px; left:21px">We perform a deep cleaning of the interior such as the dashboard, door jams, center console, trunk area, upholstered seats, and all carpets and mats. This process will remove soils and most stains. Windows are cleaned inside and out. All leather is dressed to provide a protective finish. Air fresher is available upon request.</p>
  </section>

  <section class="service mini">
    <div class="service-tag" style="width:516px">
      <svg width="516" height="40" viewBox="0 0 516 40"><polygon points="0,0 516,0 478,40 0,40" fill="#fbed22"/></svg>
      <h2 style="padding-left:31px">Mini Detail/ VIP Service Includes:</h2>
    </div>
    <p class="justified" style="top:73px; left:14px">Ridgeview Special Wash with triple polish wax, Glavenor Shield protectant, tire shine, and a detailed and gentle cleaning of the upholstery. 4 rubber or carpet mats are shampooed. All interior surfaces are dressed including dashboard, door panels, center console. This is followed by a detailed carpet and upholstery vacuum with compressed air to remove dirt from hard to reach places. For added shine ask about adding on our express wax service to your mini detail package.</p>
  </section>

  <section class="service headlight">
    <div class="service-tag" style="width:387px">
      <svg width="387" height="40" viewBox="0 0 387 40"><polygon points="0,0 387,0 349,40 0,40" fill="#fbed22"/></svg>
      <h2 style="padding-left:40px">Headlight Restoration:</h2>
    </div>
    <p class="justified" style="top:78px">This shop proudly offers the Headlight Service, which can polish or restore your headlight to a clear, safe condition at a fraction of the cost of headlight replacement! Restore the lens to a clear, shiny &amp; safe condition.</p>
  </section>
</main>
</body>
</html>
```